Belvant Systems Business Card

Utilize the newly designed logo to create a polished, professional 2-sided business card for this IT Services company.

Target Market(s)

IT Professionals many in the telecommunications and medical industries.

Industry/Entity Type

Business

Requirements
Must have
• Use of new logo, identified color palette and font: Albertus MT Std Regular.

```html
<!DOCTYPE html>
<html lang="en">
<head>
<meta charset="utf-8">
<title>Belvant Systems Business Card</title>
<link rel="stylesheet" href="https://fonts.googleapis.com/css2?family=Marcellus&family=Arimo:wght@700&family=Roboto+Condensed:wght@400&display=swap">
<style>
  :root {
    --navy: #1f3f94;
    --band-blue: #1a8be6;
    --sky: #2aa3e2;
    --mid-blue: #3f7fd0;
    --text-grey: #4a4a4a;
    --card: #ffffff;
    --stage-top: #b3b1b2;
    --stage-bottom: #262626;
  }
  * { margin: 0; padding: 0; box-sizing: border-box; }
  html, body { width: 1200px; height: 800px; overflow: hidden; }
  body {
    position: relative;
    background: linear-gradient(180deg, var(--stage-top) 0%, var(--stage-bottom) 100%);
    font-family: "Roboto Condensed", Arial, sans-serif;
  }
  .card {
    position: absolute;
    width: 582px;
    height: 333px;
    background: var(--card);
    overflow: hidden;
  }
  /* Front */
  .card-front { left: 60px; top: 50px; }
  .brand-mark {
    position: absolute;
    left: 44px; top: 60px;
    width: 156px; height: 156px;
    border-radius: 50%;
    background: var(--mid-blue);
  }
  .brand-name {
    position: absolute;
    left: 226px; top: 80px;
    font-family: "Marcellus", Georgia, serif;
    color: var(--navy);
    line-height: 1;
  }
  .brand-name .line-primary { display: block; font-size: 66px; letter-spacing: 1px; }
  .brand-name .line-secondary { display: block; font-size: 35px; letter-spacing: 3px; margin-top: 14px; }
  .front-web {
    position: absolute;
    left: 137px; top: 301px;
    width: 310px; height: 32px;
    background: var(--sky);
    color: #fff;
    font-size: 20px;
    line-height: 32px;
    text-align: center;
  }
  /* Back */
  .card-back { left: 566px; top: 414px; }
  .holder-name {
    position: absolute;
    left: 20px; top: 24px;
    font-family: "Arimo", Arial, sans-serif;
    font-weight: 700;
    font-size: 25px;
    color: var(--navy);
    letter-spacing: 0.3px;
  }
  .holder-title {
    position: absolute;
    left: 20px; top: 52px;
    font-size: 20px;
    color: var(--text-grey);
  }
  .contact-list {
    position: absolute;
    left: 16px; top: 141px;
    list-style: none;
  }
  .contact-list li {
    display: flex;
    align-items: center;
    height: 23.5px;
    font-size: 17px;
    color: var(--text-grey);
  }
  .contact-list svg { width: 16px; height: 16px; margin-right: 8px; flex: none; }
  .back-mark {
    position: absolute;
    left: 391px; top: 92px;
    width: 120px; height: 120px;
    border-radius: 50%;
    background: var(--mid-blue);
  }
  .back-brand {
    position: absolute;
    left: 351px; top: 222px;
    width: 200px;
    text-align: center;
    font-family: "Marcellus", Georgia, serif;
    font-size: 22px;
    color: var(--navy);
    letter-spacing: 1px;
  }
  .footer-band { position: absolute; left: 0; top: 280px; width: 582px; height: 53px; }
  .back-web {
    position: absolute;
    left: 16px; top: 292px;
    display: flex; align-items: center;
    font-size: 17px;
    color: #fff;
  }
  .back-web svg { width: 16px; height: 16px; margin-right: 8px; }
</style>
</head>
<body>
  <section class="card card-front" aria-label="Business card front">
    <div class="brand-mark"></div>
    <h1 class="brand-name">
      <span class="line-primary">BELVANT</span>
      <span class="line-secondary">SYSTEMS</span>
    </h1>
    <div class="front-web">www.belvantsystems.com</div>
  </section>

  <section class="card card-back" aria-label="Business card back">
    <h2 class="holder-name">YOUR COMPLETE NAME</h2>
    <p class="holder-title">Your Job Title</p>
    <ul class="contact-list">
      <li>
        <svg viewBox="0 0 16 16" aria-hidden="true"><path fill="#1f3f94" d="M4 1.5l2.2 3-1.3 1.4c.8 1.8 2.3 3.4 4.2 4.3l1.4-1.3 3 2.2-1.3 2.5C7 13.6 2.4 9 1.5 3.4z"/></svg>
        01 23456789
      </li>
      <li>
        <svg viewBox="0 0 16 16" aria-hidden="true"><rect x="4" y="1" width="8" height="14" rx="1.5" fill="#1f3f94"/><rect x="5.5" y="3" width="5" height="4" fill="#fff"/><circle cx="8" cy="11.5" r="1.2" fill="#fff"/></svg>
        09 176543210
      </li>
      <li>
        <svg viewBox="0 0 16 16" aria-hidden="true"><rect x="1.5" y="4" width="13" height="9" fill="none" stroke="#1f3f94" stroke-width="1.4"/><path d="M1.5 4l6.5 5 6.5-5" fill="none" stroke="#1f3f94" stroke-width="1.4"/></svg>
        emailme@myaddress.com
      </li>
    </ul>

    <div class="back-mark"></div>
    <div class="back-brand">BELVANT SYSTEMS</div>

    <svg class="footer-band" viewBox="0 0 582 53" aria-hidden="true">
      <path fill="var(--band-blue)" d="M0 0H196C222 0 224 38 252 38H582V53H0Z"/>
    </svg>
    <div class="back-web">
      <svg viewBox="0 0 16 16" aria-hidden="true"><g fill="none" stroke="#fff" stroke-width="1.2"><circle cx="8" cy="8" r="6.3"/><ellipse cx="8" cy="8" rx="2.8" ry="6.3"/><path d="M1.7 8h12.6M2.6 4.8h10.8M2.6 11.2h10.8"/></g></svg>
      www.yourwebsite.com
    </div>
  </section>
</body>
</html>
```